Walter Hobbs PA Card Logo

Current logo attached. Its 25 year old logo I have used. Looking for a new fresh elegant professional look/design for a law firm that has high net worth clientele and is estate planning business law firm. Firm mis in Palm Beach Florida.
One sided card linen stock white will be used. Logo section name section. Logo should include nice elegant design using the letter "G" perhapa (I am not wed to current font of the G on current logo.) Be creative there with logo design. My initials are WH.......color scheme I figure 3 tone... Raised Gold Foil, Blue name of firm = Walter Hobbs, P.A. My practice focus is Family and Business Asset Protection. My name is Walter W. Hobbs, Esq. Practice specialties include Asset Protection trusts, Business Succession Planning, LLC law, Estate Planning, Medicaid Planning (Maybe put those topics in bullets in a section of card. Bottom of card can be reserved smaller print address phone website and email address. Address section is not as important as logo and topics of practice on front. I foresee address section can be in dark blue. MY name and Topics dark blue as well.
Target Market(s)
affluent; business owners executives; wealth 2-10 million net worth
Industry/Entity Type
business law and estate planning
Contact Information for Business Card
White thick linen one sided

```html
<!DOCTYPE html>
<html lang="en">
<head>
<meta charset="utf-8">
<title>Walter Hobbs, P.A. – Business Card</title>
<link rel="stylesheet" href="https://fonts.googleapis.com/css2?family=Cinzel:wght@600&family=Open+Sans:wght@400;600;700&display=swap">
<style>
  :root {
    --backdrop: #ebe9e9;
    --paper: #ffffff;
    --navy: #2a3397;
    --gold: #c99a3a;
    --gold-light: #fcf9a6;
    --divider: #e0a526;
    --sans: "Open Sans", Arial, sans-serif;
    --serif: "Cinzel", "Times New Roman", serif;
  }
  * { margin: 0; padding: 0; box-sizing: border-box; }
  html, body { width: 1200px; height: 1200px; overflow: hidden; }
  body { background: var(--backdrop); position: relative; font-family: var(--sans); }

  .card { position: absolute; width: 805px; height: 460px; overflow: hidden; }
  .card--front { left: 49px; top: 102px; background: var(--paper); }
  .card--back  { left: 361px; top: 653px; background: var(--navy); }

  .foil-band {
    position: absolute; left: 0; bottom: 0; width: 100%; height: 27px;
    background: linear-gradient(90deg, var(--gold) 0%, var(--gold) 14%, #e6cd6c 35%, var(--gold-light) 52%, #e8d070 68%, var(--gold) 86%, var(--gold) 100%);
  }

  .centered { position: absolute; left: 0; width: 100%; text-align: center; }

  /* Front */
  .brand-mark {
    position: absolute; left: 0; top: 110px; width: 100%;
    display: flex; align-items: center; justify-content: center; gap: 14px;
  }
  .brand-mark__square { width: 24px; height: 24px; background: var(--gold); }
  .brand-mark__name {
    font-family: var(--sans); font-weight: 600; font-size: 32px; line-height: 40px;
    color: var(--gold); letter-spacing: 1px;
  }
  .firm-name {
    top: 200px; font-family: var(--serif); font-weight: 600;
    font-size: 44px; line-height: 48px; color: var(--navy); letter-spacing: 0.5px;
  }
  .firm-rule {
    position: absolute; left: 219px; top: 251px; width: 368px; height: 2px; background: var(--divider);
  }
  .firm-tagline {
    top: 256px; font-size: 33px; line-height: 36px; color: var(--navy); font-weight: 400;
  }
  .services {
    top: 364px; font-size: 17px; line-height: 19px; color: var(--navy); font-weight: 400;
  }
  .services .sep { color: var(--divider); padding: 0 4px; font-size: 14px; }

  /* Back */
  .attorney-name {
    top: 66px; font-weight: 700; font-size: 55px; line-height: 64px; color: #fff; letter-spacing: 2px;
  }
  .attorney-title {
    top: 126px; font-weight: 400; font-size: 29px; line-height: 36px; color: #fff; letter-spacing: 2px;
  }
  .contact { top: 240px; color: #fff; font-size: 24px; line-height: 30px; }
  .contact li { list-style: none; }
</style>
</head>
<body>

<section class="card card--front" aria-label="Card front">
  <div class="brand-mark">
    <span class="brand-mark__square"></span>
    <span class="brand-mark__name">Walter Hobbs PA</span>
  </div>
  <div class="centered firm-name">Walter Hobbs, P.A.</div>
  <div class="firm-rule"></div>
  <div class="centered firm-tagline">ELDER LAW ATTORNEY</div>
  <div class="centered services">
    <p>ASSET PROTECTION TRUSTS<span class="sep">|</span>BUSINESS SUCCESSION PLANNING</p>
    <p>MEDICAID PLANNING<span class="sep">|</span>LLC LAW<span class="sep">|</span>ESTATE PLANNING</p>
  </div>
  <div class="foil-band"></div>
</section>

<section class="card card--back" aria-label="Card back">
  <div class="centered attorney-name">WALTER W. HOBBS, ESQ</div>
  <div class="centered attorney-title">CERTIFIED ELDER LAW ATTORNEY</div>
  <ul class="centered contact">
    <li>name@email.com</li>
    <li>+1 561-555-0148</li>
    <li>2840 Harbor View Dr, Boynton Beach,</li>
    <li>FL 33426, United States</li>
    <li>www.coastalestatecounsel.com</li>
  </ul>
  <div class="foil-band"></div>
</section>

</body>
</html>
```